Classic Minimalistic Business Card

Design a classic, minimalistic Business Card. Please find inspiration in the attached Classic Minimalistic examples. My information:
Name: Glen Whitacre
Company: Whitacre Holdings
Logo: WC
Address: 1800 N Corliss Ave, Suite 420 | Geneva, IL 60187
Phone: 630-555-0172
Email: glenwhitacre@tvm.example
Slogan: Stewarding Wealth With Purpose

Feel free to leave out any of the information above except my name.

I have selected Double-sided, but I am also open to Single-sided

Target Market(s)

22-70. income greater than 150k/year

Industry/Entity Type

Finance

Contact Information for Business Card

See Project Description

Requirements
Must have
• Ivory or "antiqued" background similar to the reference pictures

```html
<!DOCTYPE html>
<html lang="en">
<head>
<meta charset="UTF-8">
<title>Whitacre Holdings — Business Card</title>
<link rel="stylesheet" href="https://fonts.googleapis.com/css2?family=Pinyon+Script&family=Courier+Prime:wght@400&display=swap">
<style>
  :root {
    --backdrop: #cfd3d8;
    --card-kraft: #d3c0ae;
    --ink: #2a2a2c;
    --ink-soft: #3a3a3d;
  }
  * { margin: 0; padding: 0; box-sizing: border-box; }
  html, body {
    width: 1200px;
    height: 800px;
    overflow: hidden;
    background: var(--backdrop);
  }
  .canvas {
    position: relative;
    width: 1200px;
    height: 800px;
    display: flex;
    flex-direction: column;
    align-items: center;
    justify-content: center;
    gap: 36px;
  }
  .card {
    position: relative;
    width: 542px;
    height: 306px;
    background: var(--card-kraft);
    color: var(--ink);
    box-shadow: 0 2px 6px rgba(40, 40, 50, 0.18);
    text-align: center;
  }
  .card p, .card h1, .card h2 { white-space: nowrap; }

  /* Front side */
  .card--front .company-name {
    position: absolute;
    left: 0; right: 0;
    top: 118px;
    font-family: "Courier Prime", monospace;
    font-weight: 400;
    font-size: 34px;
    line-height: 1;
    letter-spacing: 2px;
    color: var(--ink);
  }
  .card--front .slogan {
    position: absolute;
    left: 0; right: 0;
    top: 178px;
    font-family: "Courier Prime", monospace;
    font-size: 11px;
    line-height: 1;
    letter-spacing: 3.6px;
    text-transform: uppercase;
    color: var(--ink-soft);
  }

  /* Back side */
  .card--back .person-name {
    position: absolute;
    left: 0; right: 0;
    top: 128px;
    font-family: "Pinyon Script", cursive;
    font-weight: 400;
    font-size: 46px;
    line-height: 1;
    color: var(--ink);
  }
  .card--back .contact-line {
    position: absolute;
    left: 0; right: 0;
    top: 176px;
    font-family: "Courier Prime", monospace;
    font-size: 11px;
    line-height: 1;
    letter-spacing: 2px;
    text-transform: uppercase;
    color: var(--ink-soft);
  }
  .card--back .address-line {
    position: absolute;
    left: 0; right: 0;
    bottom: 14px;
    font-family: "Courier Prime", monospace;
    font-size: 11px;
    line-height: 1;
    letter-spacing: 1.8px;
    text-transform: uppercase;
    color: var(--ink-soft);
  }
</style>
</head>
<body>
  <main class="canvas">
    <section class="card card--front" aria-label="Card front">
      <h1 class="company-name">Whitacre Holdings</h1>
      <p class="slogan">Stewarding Wealth With Purpose</p>
    </section>
    <section class="card card--back" aria-label="Card back">
      <h2 class="person-name">Glen Whitacre</h2>
      <p class="contact-line">630-555-0172 | glenwhitacre@tvm.example</p>
      <p class="address-line">1800 N Corliss Ave, Suite 420 | Geneva, IL 60187</p>
    </section>
  </main>
</body>
</html>
```